Belle Lueur Hand Crafted Candles promotional flyer

Hand Crafted Soy Candles - I need a flyer to promote my candles and to give information on care of candles.I want this to use the design and colours I already have for my labels and the photo I have attached.I am aiming at a sophisticated market so would like to reflect this in the design.
Should appeal to sophisticated women who enjoy the pleasure of candles - to enhance their enjoyment of life - gives them the 'joie de vivre'.
the candles are hand crafted from all natural ingredients, environmentally friendly and with exquisite fragrances

Target Market(s)

sophisticated females

Industry/Entity Type

Promotional

Font styles to use
Script

Colors
cfeae6
ecdaeb

Requirements
Must have
• something expressing 'joie de vivre' - the enjoyment of candles
Should not have
• bright colours

```html
<!DOCTYPE html>
<html lang="en">
<head>
<meta charset="utf-8">
<title>Belle Lueur Hand Crafted Candles – Flyer</title>
<link rel="stylesheet" href="https://fonts.googleapis.com/css2?family=Parisienne&family=Cinzel:wght@400;600;700&family=Raleway:wght@300;400;700&display=swap">
<style>
:root{
  --backdrop:#3b3b3b;
  --paper:#ffffff;
  --mint:#cfeae6;
  --blush:#ecdaeb;
  --ink:#2f2f33;
  --ink-soft:#55565a;
  --muted:#7a7a80;
  --wood-dark:#5a3a22;
  --wood-light:#a8754a;
  --jar-dark:#2e2f33;
  --jar-light:#c9c9c4;
}
*{box-sizing:border-box;margin:0;padding:0}
html,body{width:1200px;height:1000px;overflow:hidden;background:var(--backdrop)}
.canvas{position:relative;width:1200px;height:1000px}
.flyer{position:absolute;left:268px;top:25px;width:664px;height:947px;background:var(--paper);overflow:hidden;font-family:'Raleway',sans-serif;color:var(--ink)}
.abs{position:absolute}
.mint-field{left:0;top:37px;width:664px;height:800px;background:var(--mint)}
.edge{left:0;width:664px}
.brand-title{left:27px;top:56px;font-family:'Parisienne',cursive;font-size:56px;font-weight:400;line-height:1;color:var(--ink)}
.tagline{left:27px;top:115px;font-family:'Cinzel',serif;font-weight:600;font-size:16px;letter-spacing:.2px}
.intro{left:27px;top:143px;font-size:13px;line-height:16px;font-weight:300;color:var(--ink-soft);white-space:nowrap}
.features{left:27px;top:199px;font-family:'Cinzel',serif;font-weight:600;font-size:16px;line-height:20.5px;letter-spacing:.3px;list-style:none;white-space:nowrap}
.section-band{left:0;height:24px;background:var(--blush);clip-path:polygon(0 0,100% 0,calc(100% - 14px) 100%,0 100%);font-family:'Cinzel',serif;font-weight:600;font-size:15px;line-height:24px;padding-left:27px;letter-spacing:.4px;white-space:nowrap}
.band-soy{top:313px;width:178px}
.band-refill{top:543px;width:308px}
.soy-points{left:30px;top:352px;list-style:none;font-size:13px;line-height:15.9px;font-weight:300;color:var(--ink-soft);white-space:nowrap}
.soy-points li{padding-left:10px;text-indent:-10px}
.soy-points li::before{content:"";display:inline-block;width:6px;height:6px;border-radius:50%;background:var(--ink-soft);margin-right:4px;vertical-align:1px}
.hl{font-family:'Cinzel',serif;font-weight:700;color:var(--ink);font-size:12.8px;letter-spacing:.2px}
.refill{left:27px;top:582px;font-size:13px;line-height:15.6px;font-weight:300;color:var(--ink-soft);white-space:nowrap}
.care-panel{left:392px;top:105px;width:260px;height:620px;background:var(--blush)}
.care-rule{left:384px;top:122px;width:276px;height:1px;background:var(--ink)}
.care-ornament{left:456px;top:88px;width:136px;height:30px;border-radius:15px;background:radial-gradient(ellipse at center,#8e8a90 0,rgba(142,138,144,.35) 45%,transparent 70%);opacity:.6}
.care-title{left:409px;top:132px;font-family:'Cinzel',serif;font-weight:400;font-size:13px;letter-spacing:.4px;white-space:nowrap}
.care-sub{left:381px;top:149px;font-size:8.8px;line-height:11px;color:var(--muted);width:210px}
.care-list{left:410px;top:195px;width:214px;list-style:none;font-size:9.2px;line-height:11.4px;color:var(--ink-soft)}
.care-list li{margin-bottom:12px;padding-left:8px;text-indent:-8px}
.care-list li::before{content:"";display:inline-block;width:5px;height:5px;border-radius:50%;background:var(--ink-soft);margin-right:3px;vertical-align:1px}
.care-list b{color:var(--ink);font-weight:700}
.photo-table{left:0;top:797px;width:664px;height:76px;background:linear-gradient(100deg,var(--wood-dark),var(--wood-light) 35%,var(--wood-dark) 60%,var(--wood-light) 85%,var(--wood-dark))}
.photo-candles{left:244px;top:653px;width:396px;height:207px;border-radius:10px 10px 4px 4px;background:linear-gradient(90deg,var(--jar-dark) 0 36%,#8e8e8a 40%,var(--jar-light) 46%,#dcdcd6 70%,#e6e6e0)}
.brand-seal{left:48px;top:722px;width:134px;height:134px;border-radius:50%;background:#e4eaec;box-shadow:0 2px 6px rgba(0,0,0,.35);display:flex;align-items:center;justify-content:center;font-family:'Cinzel',serif;font-size:16px;color:var(--ink)}
.contact{left:20px;top:885px;font-size:15px;line-height:25px;font-weight:400;color:var(--ink-soft)}
.web{right:27px;top:886px;font-family:'Cinzel',serif;font-weight:600;font-size:16px;letter-spacing:.5px;color:var(--ink)}
</style>
</head>
<body>
<div class="canvas">
  <article class="flyer">
    <div class="abs mint-field"></div>
    <svg class="abs edge" style="top:0" width="664" height="40" aria-hidden="true">
      <polygon points="0,0 664,0 664,4 0,37" fill="var(--blush)"/>
    </svg>

    <h1 class="abs brand-title">Belle Lueur</h1>
    <p class="abs tagline">– An Exuberant Enjoyment Of Life</p>
    <p class="abs intro">These candles will fill you with "a zest for life.<br>Candles are lovingly hand-poured and use only<br>the finest of ingredients and fragrances.</p>
    <ul class="abs features">
      <li>Hand Crafted Soy Candle Creations</li>
      <li>Completely Non-toxic</li>
      <li>Exquisite Fragrances</li>
      <li>Clean Burning</li>
      <li>Environmentally Friendly</li>
    </ul>

    <h2 class="abs section-band band-soy">Why Soy Wax?</h2>
    <ul class="abs soy-points">
      <li>Soft smooth wax that burns clear –<br><span class="hl">No Soot Or Smoke</span></li>
      <li>Soy wax candles <span class="hl">Burn Up To 50%</span><br><span class="hl">Longer</span> than traditional paraffin candles</li>
      <li><span class="hl">made form Soya Beans,</span> a renewable<br>natural resource that supports and sustains<br>agriculture – it is biodegradable<br>and environmentally friendly.</li>
      <li>Soy wax <span class="hl">Burns Cooler Than Paraffin</span><br><span class="hl">And Disperse The Fragrance</span><br><span class="hl">More Fully.</span></li>
    </ul>

    <h2 class="abs section-band band-refill">Containers Can Be Refilled</h2>
    <p class="abs refill">I offer a <span class="hl">Refill Service</span> -if you return you containers<br>to me I can refill with the fragrance of your choice<br>Or if you have a special container you would like to use<br>for your candle just contact me<br>for a quote.<br>I have a <span class="hl">Wide Range Of</span><br><span class="hl">Fragrances</span> - please contact me<br>for details.</p>

    <div class="abs care-panel"></div>
    <div class="abs care-ornament" role="img" aria-label="Decorative flourish above the candle care heading"></div>
    <div class="abs care-rule"></div>
    <h2 class="abs care-title">How To Care For Your Candle</h2>
    <p class="abs care-sub">the following tips will ensure you have a long lasting, fully fragranced candle</p>
    <ul class="abs care-list">
      <li>When lighting you candle for the first time, allow the wax to melt all the way to the sides of the container – this creates a 'memory' and avoids 'tunnelling' as the candle burns.</li>
      <li>Always trim the wick to about 6-8mm before re-lighting your candle. This will ensure a long lasting candle, minimise soot and remove any mushrooming of the wick from a previous burn.</li>
      <li>It is preferable to use a candle 'snuffer' to extinguish the flame or a lid if the candle has one. Alternatively, you can dip the wick into the melted wax and then straightening. This will stop the wick from smoking and help with relighting.</li>
      <li>All <b>Belle Lueur</b> candles are hand poured not massed produced – although every effort is made to ensure consistency, every candle may be different.</li>
      <li>Sometimes you may notice darker patches or wet spots - this is not a fault it is just the natural way the wax has set – it does not affect the candle in anyway.</li>
      <li>The top of the candle may also appear slightly uneven – this is just a sign of natural soy wax being hand poured.</li>
      <li>Do not leave your candle in the sunlight as it may turn a yellow colour – again this does not affect the candle in anyway – it just loses its creamy white colour.</li>
      <li>As these candles contain no preservatives or chemicals it is recommended that they should be used within 6 months.</li>
    </ul>

    <div class="abs photo-table" role="img" aria-label="Photo of a rustic wooden table surface"></div>
    <div class="abs photo-candles" role="img" aria-label="Photo of four labelled soy candles in black, clear and blue glass jars"></div>
    <div class="abs brand-seal">Belle Lueur</div>

    <svg class="abs edge" style="top:873px" width="664" height="74" aria-hidden="true">
      <rect x="0" y="0" width="664" height="74" fill="var(--paper)"/>
      <polygon points="0,74 664,74 664,36" fill="var(--blush)"/>
    </svg>
    <p class="abs contact">E: claire.mercer@example.com<br>M: 021 555 0142</p>
    <p class="abs web">WWW.MyBelleLueur.co.nz</p>
  </article>
</div>
</body>
</html>
```